Boat business cards

I'm looking for business cards with the two logos I've attached. I don't have an specific idea in mind and open to anything. All the usual info will be on the card. Name, position in company, nr, email, address, ect. The company rents out these two boats for charters and fishing.

```html
<!DOCTYPE html>
<html lang="en">
<head>
<meta charset="utf-8">
<title>Harbor Star Charters – Business Cards</title>
<link rel="stylesheet" href="https://fonts.googleapis.com/css2?family=Poppins:wght@400;500;600&family=Michroma&display=swap">
<style>
  :root{
    --canvas:#e6e8eb;
    --card:#ffffff;
    --card-soft:#f4f8fc;
    --wave-deep:#6f9fd0;
    --wave-mid:#9cc3e8;
    --wave-pale:#dcebf8;
    --ink:#1c1c1c;
    --ink-soft:#3a3f45;
    --accent-brown:#9c7a4e;
    --line:#5a86b8;
    --logo-grey:#56606b;
  }
  *{box-sizing:border-box;margin:0;padding:0}
  html,body{width:1200px;height:900px;overflow:hidden}
  body{background:var(--canvas);font-family:"Poppins",sans-serif;position:relative}
  .card{position:absolute;left:250px;width:700px;height:400px;border-radius:28px;overflow:hidden;background:var(--card);box-shadow:0 6px 18px rgba(0,0,0,.15)}
  .card--back{top:30px}
  .card--front{top:470px}
  .card__waves{position:absolute;inset:0;width:700px;height:400px}
  .logo{position:absolute;display:flex;align-items:center;gap:10px;font-family:"Poppins",sans-serif;font-weight:600;white-space:nowrap}
  .logo__dot{width:14px;height:14px;border-radius:50%;display:inline-block}
  .logo--primary{color:var(--ink);font-size:34px}
  .logo--primary .logo__dot{background:var(--ink)}
  .logo--secondary{color:var(--logo-grey);font-size:28px}
  .logo--secondary .logo__dot{background:var(--logo-grey)}
  .card--back .logo--primary{left:70px;top:175px}
  .card--back .logo--secondary{left:420px;top:62px}
  .card--front .logo--primary{left:60px;top:145px}
  .card--front .logo--secondary{left:430px;top:55px}
  .person{position:absolute;left:45px;top:268px}
  .person__name{font-family:"Michroma",sans-serif;font-size:24px;color:var(--ink);line-height:1.2}
  .person__role{font-family:"Michroma",sans-serif;font-size:15px;color:var(--accent-brown);margin-top:2px}
  .contact{position:absolute;left:45px;top:338px;font-size:16px;color:var(--ink-soft);line-height:26px}
  .contact__row{display:flex;align-items:center;gap:10px}
  .contact__icon{width:18px;height:18px;flex:none}
  .divider{position:absolute;left:245px;top:306px;width:425px;height:1.5px;background:var(--line)}
  .address{position:absolute;left:430px;top:318px;display:flex;gap:10px;font-size:15px;color:var(--ink-soft);line-height:22px}
  .address .contact__icon{margin-top:3px}
</style>
</head>
<body>

<section class="card card--back" aria-label="Card back">
  <svg class="card__waves" viewBox="0 0 700 400" aria-hidden="true">
    <rect width="700" height="400" fill="var(--card-soft)"/>
    <path d="M700,100 C560,110 470,230 380,290 C290,350 150,360 0,330 L0,400 L700,400 Z" fill="var(--wave-pale)"/>
    <path d="M700,125 C565,135 480,250 390,310 C300,365 160,375 0,355 L0,400 L700,400 Z" fill="var(--wave-mid)"/>
    <path d="M700,150 C575,160 495,270 405,330 C320,385 170,392 0,385 L0,400 L700,400 Z" fill="var(--wave-deep)"/>
  </svg>
  <div class="logo logo--primary"><span class="logo__dot"></span>Harbor Star</div>
  <div class="logo logo--secondary"><span class="logo__dot"></span>Sea Runner</div>
</section>

<section class="card card--front" aria-label="Card front">
  <svg class="card__waves" viewBox="0 0 700 400" aria-hidden="true">
    <rect width="700" height="400" fill="var(--card)"/>
    <path d="M0,235 C170,180 420,250 700,80 L700,400 L0,400 Z" fill="var(--wave-mid)"/>
    <path d="M0,262 C180,210 430,270 700,108 L700,400 L0,400 Z" fill="var(--wave-pale)"/>
    <path d="M0,290 C190,240 440,290 700,140 L700,400 L0,400 Z" fill="var(--card-soft)"/>
  </svg>
  <div class="logo logo--primary"><span class="logo__dot"></span>Harbor Star</div>
  <div class="logo logo--secondary"><span class="logo__dot"></span>Sea Runner</div>

  <div class="person">
    <p class="person__name">Daniel Reyes</p>
    <p class="person__role">Managing Director</p>
  </div>
  <div class="divider"></div>

  <div class="contact">
    <p class="contact__row">
      <svg class="contact__icon" viewBox="0 0 24 24" aria-hidden="true"><path d="M6.6 10.8a15.1 15.1 0 0 0 6.6 6.6l2.2-2.2a1 1 0 0 1 1-.25 11.4 11.4 0 0 0 3.6.57 1 1 0 0 1 1 1V20a1 1 0 0 1-1 1A17 17 0 0 1 3 4a1 1 0 0 1 1-1h3.5a1 1 0 0 1 1 1c0 1.25.2 2.45.57 3.57a1 1 0 0 1-.25 1z" fill="var(--wave-deep)"/></svg>
      555-013-2847
    </p>
    <p class="contact__row">
      <svg class="contact__icon" viewBox="0 0 24 24" aria-hidden="true"><rect x="2" y="5" width="20" height="14" rx="1" fill="var(--wave-deep)"/><path d="M2.5 5.5 12 13l9.5-7.5" fill="none" stroke="#fff" stroke-width="1.5"/></svg>
      daniel@harborstar.com
    </p>
  </div>

  <div class="address">
    <svg class="contact__icon" viewBox="0 0 24 24" aria-hidden="true"><path d="M12 2a7 7 0 0 0-7 7c0 5 7 13 7 13s7-8 7-13a7 7 0 0 0-7-7zm0 9.5A2.5 2.5 0 1 1 12 6.5a2.5 2.5 0 0 1 0 5z" fill="var(--wave-deep)"/></svg>
    <p>418 Lakeshore Drive<br>Suite 210, Port Haven, MI 49100</p>
  </div>
</section>

</body>
</html>
```